Design Template for use with our Career Cluster Maps

***Update 11/24*** - Please see K7V Work Ready Model (attached) for color scheme and targeted look and feel. Also, focus on content displayed in the Construction Cluster document (attached). All information displayed in the Construction Cluster document needs to be included in the design. Need a clean, simple design. Unique ideas for organizing content are welcomed.

We need a unique design for our curriculum maps. I have two copies that are models, both are good but are not unique to us as a company. We provide the data that allows the templates to be filled in by clients, so don't worry about the actual data, just what can we design around how the data is displayed. Our main website is trailforjobs.example , feel free to use anything from that site as well as the colors. I am attaching the 2 designs as well as some unique pictures that can be incorporated. The design when final will go into our software platform and the data will be pulled and placed for schools to use automatically, again looking for a design that captures the idea between the job market and job preparedness. I have added an additional document that shows "all the pathways" and how our software pulls the data and puts on a template. The template we desire needs to be updated, the two additional files show how our clients have tried to update the template with a better look and feel. We want a better look and feel in our platform.

Please post the design as a PDF but we need the In-Design files so that we can edit and use within our system

```html
<!DOCTYPE html>
<html lang="en">
<head>
<meta charset="utf-8">
<title>Career Cluster Maps – K7V</title>
<link href="https://fonts.googleapis.com/css2?family=Inter:ital,wght@0,400;0,500;0,600;0,700;0,800;1,400&display=swap" rel="stylesheet">
<style>
  :root {
    --navy: #0d3a6e;
    --sky: #2fa6dc;
    --sky-light: #84d8fb;
    --orange: #f29312;
    --ink: #111111;
    --muted: #555555;
    --row-grey: #e3e3e3;
    --divider: #d6d6d6;
    --paper: #ffffff;
  }
  * { box-sizing: border-box; margin: 0; padding: 0; }
  html, body { width: 1200px; height: 800px; overflow: hidden; background: var(--paper); }
  body { font-family: "Inter", Arial, sans-serif; color: var(--ink); position: relative; }

  .brand { position: absolute; top: 42px; right: 80px; display: flex; align-items: center; gap: 9px; }
  .brand-mark { width: 16px; height: 16px; background: var(--orange); }
  .brand-text { display: flex; flex-direction: column; }
  .brand-name { color: var(--navy); font-weight: 600; font-size: 16px; line-height: 1.15; }
  .brand-tagline { color: var(--muted); font-size: 10.5px; margin-top: 1px; }

  .page-title {
    position: absolute; left: 82px; top: 58px;
    font-size: 50px; font-weight: 800; color: var(--navy); letter-spacing: -1.5px;
  }

  .intro {
    position: absolute; left: 82px; top: 131px; width: 1038px;
    font-size: 15px; line-height: 19.6px; text-align: justify; color: var(--ink);
  }

  .data-section { position: absolute; left: 82px; top: 315px; width: 1038px; }
  .section-rule { height: 3px; background: var(--sky-light); }
  .section-title {
    text-align: center; color: var(--sky); font-size: 26px; font-weight: 700;
    letter-spacing: -0.8px; margin-top: 4px; line-height: 32px;
  }

  .cluster-table { width: 100%; border-collapse: collapse; table-layout: fixed; }
  .cluster-table th {
    background: var(--sky-light); font-size: 15.5px; font-weight: 600; height: 26px;
    letter-spacing: -0.4px; border-left: 1px solid var(--paper);
  }
  .cluster-table th:first-child { border-left: none; }
  .cluster-table td { font-size: 15.5px; vertical-align: middle; border-left: 1px solid var(--divider); }
  .cluster-table td:first-child { border-left: none; }
  .col-category { width: 188px; }
  .col-description { width: 363px; }
  .cat { text-align: center; font-weight: 600; letter-spacing: -0.4px; line-height: 20px; padding-right: 20px; }
  .desc { font-weight: 600; letter-spacing: -0.4px; line-height: 20px; padding: 0 20px 0 39px; }
  .app { padding: 6px 9px 6px 43px; line-height: 19.6px; text-align: justify; font-size: 14.6px; letter-spacing: -0.2px; }
  .app strong { font-weight: 700; }
  .row-entry { height: 122px; }
  .row-openings { height: 96px; background: var(--row-grey); }
  .row-wage { height: 104px; }

  .footnotes {
    position: absolute; left: 82px; top: 718px;
    font-size: 12.5px; font-style: italic; line-height: 16px; color: var(--ink);
  }
</style>
</head>
<body>
  <div class="brand">
    <span class="brand-mark"></span>
    <div class="brand-text">
      <span class="brand-name">Trailforge Learning</span>
      <span class="brand-tagline">Skills for the road ahead</span>
    </div>
  </div>

  <h1 class="page-title">CAREER CLUSTER MAPS</h1>

  <p class="intro">The K7V Career Cluster Maps provide an overview of regional high-demand occupations associated with various job zones (i.e., levels of education and training). The purpose of these maps is to assist educators and students in developing awareness of entry and exit points within a particular career field. The maps have been developed to align with the National Career Pathways Framework and rely on the JobScope job zone classification system to accurately assign occupations to job zones. Labor market data displayed in the cluster maps was collected from state and regional labor departments to reveal market demand and median wages for each occupation. In using these maps, educators and students can quickly gain a sense of potential highvalue career opportunities and the level of education and training needed to prepare for these professions. This can promote the alignment of education practices with regional careers and assist students in making informed career decisions that take into account regional labor market demands.</p>

  <section class="data-section">
    <div class="section-rule"></div>
    <h2 class="section-title">CAREER CLUSTER MAP DATA</h2>
    <table class="cluster-table">
      <colgroup>
        <col class="col-category"><col class="col-description"><col>
      </colgroup>
      <thead>
        <tr><th>Data Category</th><th>Data Description</th><th>Potential Application</th></tr>
      </thead>
      <tbody>
        <tr class="row-entry">
          <td class="cat">Occupations by<br>Job Zone</td>
          <td class="desc">Occupations listed by highest projected demand within each job zone</td>
          <td class="app"><strong>Understanding Entry and Exit Points</strong> - Educators and students can identify employment opportunities that are highest in demand at various education levels. This can be used to encourage informed decisions about when to enter and exit education/training programs.</td>
        </tr>
        <tr class="row-openings">
          <td class="cat">Annual Openings</td>
          <td class="desc">Projected annual openings displayed for each occupation</td>
          <td class="app"><strong>Evaluating Employment Opportunity</strong> - Occupations that are higher in annual openings offer more opportunity for students. Educational practices can be directed toward preparing students for occupations that are highest in demand.</td>
        </tr>
        <tr class="row-wage">
          <td class="cat">Median Wage</td>
          <td class="desc">Median wage data listed for each occupation</td>
          <td class="app"><strong>Assessing Occupation Value</strong> - Data related to median wages can be used to determine which occupations offer the most value to students. Career readiness efforts can target high-value occupations with higher wages, as well as higher annual openings.</td>
        </tr>
      </tbody>
    </table>
  </section>

  <div class="footnotes">
    <p>* Few occupations in these pathways require education at this level.</p>
    <p>*** = Insufficient Data</p>
  </div>
</body>
</html>
```